business card deign

Logo needs the following on it.
1. attached logo
2. Tagline - "Cold drinks, good tunes and a party that never stops!"
3. Name- Delia Fenwick, Founder and CPO
4. Address - 418 E. Harlow Avenue, Ste 2204, Palmora, FL. 33719
5. Phone - 612.555.0187

```html
<!DOCTYPE html>
<html lang="en">
<head>
<meta charset="utf-8">
<title>Chillwell Business Card</title>
<link rel="stylesheet" href="https://fonts.googleapis.com/css2?family=Montserrat:wght@400;700&display=swap">
<style>
  :root {
    --bg: #e9e6e1;
    --card: #ffffff;
    --ink: #111111;
    --muted: #333333;
    --paper-line: #ffffff;
  }
  html, body {
    margin: 0;
    padding: 0;
    width: 1200px;
    height: 821px;
    overflow: hidden;
    background: var(--bg);
    font-family: "Montserrat", sans-serif;
  }
  .stage {
    position: relative;
    width: 1200px;
    height: 821px;
  }
  .card {
    position: absolute;
    width: 520px;
    height: 300px;
    background: var(--card);
    border-radius: 22px;
    overflow: hidden;
    box-shadow: 0 10px 24px rgba(0,0,0,0.18);
  }
  .card--front { left: 70px; top: 90px; }
  .card--back { left: 610px; top: 431px; }

  .brand {
    display: flex;
    align-items: center;
    justify-content: center;
    gap: 12px;
  }
  .brand__dot {
    width: 14px;
    height: 14px;
    border-radius: 50%;
    background: var(--ink);
    flex: none;
  }
  .wordmark {
    font-family: "Montserrat", sans-serif;
    font-weight: 700;
    color: var(--ink);
    margin: 0;
    line-height: 1;
  }
  .card--front .brand {
    position: absolute;
    left: 0;
    right: 0;
    top: 100px;
  }
  .card--front .wordmark { font-size: 44px; }
  .tagline-band {
    position: absolute;
    left: 0;
    right: 0;
    top: 222px;
    height: 26px;
    background: var(--ink);
    display: flex;
    align-items: center;
    justify-content: center;
  }
  .tagline {
    margin: 0;
    color: var(--paper-line);
    font-size: 13px;
    font-weight: 400;
  }

  .card--back .logo-block {
    position: absolute;
    left: 20px;
    top: 0;
    width: 240px;
    height: 230px;
  }
  .card--back .brand { height: 100%; gap: 9px; }
  .card--back .brand__dot { width: 11px; height: 11px; }
  .card--back .wordmark { font-size: 30px; }
  .divider {
    position: absolute;
    left: 268px;
    top: 36px;
    width: 1.5px;
    height: 160px;
    background: var(--ink);
  }
  .details {
    position: absolute;
    left: 290px;
    top: 40px;
    width: 215px;
    color: var(--ink);
  }
  .details__name {
    margin: 0;
    font-size: 20px;
    font-weight: 700;
  }
  .details__title {
    margin: 2px 0 16px;
    font-size: 13px;
    color: var(--muted);
  }
  .details__phone {
    margin: 0 0 14px;
    font-size: 13px;
    display: flex;
    align-items: center;
    gap: 6px;
  }
  .details__address {
    margin: 0;
    font-size: 12.5px;
    line-height: 1.4;
  }
  .wave {
    position: absolute;
    left: 0;
    bottom: 0;
    width: 520px;
    height: 120px;
  }
</style>
</head>
<body>
<main class="stage">
  <section class="card card--front">
    <div class="brand">
      <span class="brand__dot"></span>
      <h1 class="wordmark">Chillwell</h1>
    </div>
    <div class="tagline-band">
      <p class="tagline">Cold drinks, good tunes and a party that never stops!</p>
    </div>
  </section>

  <section class="card card--back">
    <div class="logo-block">
      <div class="brand">
        <span class="brand__dot"></span>
        <p class="wordmark">Chillwell</p>
      </div>
    </div>
    <div class="divider"></div>
    <div class="details">
      <p class="details__name">Delia Fenwick</p>
      <p class="details__title">Founder and CPO</p>
      <p class="details__phone">
        <svg width="12" height="12" viewBox="0 0 24 24" aria-hidden="true">
          <path fill="#111" d="M6.6 10.8a15.1 15.1 0 0 0 6.6 6.6l2.2-2.2a1 1 0 0 1 1-.25 11.4 11.4 0 0 0 3.6.57 1 1 0 0 1 1 1V20a1 1 0 0 1-1 1A17 17 0 0 1 3 4a1 1 0 0 1 1-1h3.5a1 1 0 0 1 1 1c0 1.25.2 2.45.57 3.57a1 1 0 0 1-.25 1z"/>
        </svg>
        612.555.0187
      </p>
      <p class="details__address">418 E. Harlow Avenue, Ste<br>2204, Palmora, FL. 33719</p>
    </div>
    <svg class="wave" viewBox="0 0 520 120" preserveAspectRatio="none" aria-hidden="true">
      <path fill="#111" d="M0 120 L0 92 C120 60 220 100 330 70 C420 46 480 20 520 14 L520 120 Z"/>
      <path fill="none" stroke="#fff" stroke-width="3" d="M0 104 C120 72 220 112 330 82 C420 58 480 32 520 26"/>
    </svg>
  </section>
</main>
</body>
</html>
```